Webbanner-Design für Blog gesucht
Zielgruppe
Es geht um ein privates Blog. Inhalte des Blogs werden Gedanken zu Zitaten (aus Büchern, Film, Kino, Altertum, usw), Sprichwörtern, Gedichten usw sein. Der Titel des Blogs wird 'sinnesfaden' sein. Es wird teils nachdenklich, teils humorvoll zugehen. Technische Basis: Wordpress
Aufgabenstellung
Der Banner soll oben eingebunden werden, und soll den Begriff 'Sinnesfaden' enthalten.

```html
<!DOCTYPE html>
<html lang="de">
<head>
<meta charset="utf-8">
<title>Sinnesfaden – Banner</title>
<link rel="stylesheet" href="https://fonts.googleapis.com/css2?family=Archivo+Black&family=Montserrat:wght@500&display=swap">
<style>
  :root {
    --ink: #262626;
    --paper: #ffffff;
    --mist: #d9dcdb;
    --mist-soft: #e9ebea;
  }
  html, body {
    margin: 0;
    padding: 0;
    overflow: hidden;
    background: var(--paper);
  }
  .banner {
    position: relative;
    width: 1200px;
    height: 322px;
    overflow: hidden;
    background: var(--paper);
  }
  .banner__layer {
    position: absolute;
    inset: 0;
  }
  .brand {
    position: absolute;
    left: 473px;
    top: 72px;
    display: flex;
    align-items: center;
    gap: 10px;
  }
  .brand__dot {
    width: 27px;
    height: 27px;
    border-radius: 50%;
    background: var(--ink);
  }
  .brand__name {
    font-family: "Archivo Black", sans-serif;
    font-size: 16px;
    letter-spacing: 0.58em;
    color: var(--ink);
    text-transform: uppercase;
  }
  .topics {
    position: absolute;
    left: 234px;
    top: 214px;
    width: 732px;
    height: 44px;
    background: var(--ink);
  }
  .topics__mark {
    position: absolute;
    left: 2px;
    top: -14px;
    font-family: "Archivo Black", sans-serif;
    font-size: 64px;
    line-height: 1;
    color: var(--paper);
  }
  .topics__list {
    position: absolute;
    left: 182px;
    top: 0;
    height: 44px;
    margin: 0;
    padding: 0;
    list-style: none;
    display: flex;
    align-items: center;
    font-family: "Montserrat", sans-serif;
    font-weight: 500;
    font-size: 15px;
    letter-spacing: 0.27em;
    color: var(--paper);
  }
  .topics__list li { margin-right: 22px; }
  .topics__list li:nth-child(2),
  .topics__list li:nth-child(3) { margin-right: 30px; }
</style>
</head>
<body>
<div class="banner">
  <svg class="banner__layer" width="1200" height="322" viewBox="0 0 1200 322">
    <defs>
      <linearGradient id="quote-fill" x1="0" y1="0" x2="1" y2="1">
        <stop offset="0" stop-color="var(--mist)"/>
        <stop offset="1" stop-color="var(--mist-soft)"/>
      </linearGradient>
    </defs>
    <rect role="img" aria-label="Zwei große Anführungszeichen als Dekoration, oben links"
          x="0" y="-40" width="336" height="222" rx="60" fill="url(#quote-fill)"/>
    <rect role="img" aria-label="Zwei große Anführungszeichen als Dekoration, rechts"
          x="873" y="72" width="312" height="220" rx="60" fill="url(#quote-fill)"/>

    <g class="lines lines--light" fill="var(--mist)">
      <rect x="362" y="24" width="50" height="3.5" rx="1.75"/>
      <rect x="362" y="34" width="50" height="3.5" rx="1.75"/>
      <rect x="362" y="44" width="50" height="3.5" rx="1.75"/>
    </g>
    <g class="lines lines--paper" fill="var(--paper)">
      <rect x="94" y="74" width="50" height="4" rx="2"/>
      <rect x="94" y="84" width="50" height="4" rx="2"/>
      <rect x="94" y="94" width="50" height="4" rx="2"/>
      <rect x="1053" y="151" width="41" height="4" rx="2"/>
      <rect x="1053" y="161" width="41" height="4" rx="2"/>
      <rect x="1053" y="171" width="41" height="4" rx="2"/>
    </g>
    <g class="lines lines--ink" fill="var(--ink)">
      <rect x="312" y="97" width="89" height="9" rx="4.5"/>
      <rect x="306" y="113" width="65" height="9" rx="4.5"/>
      <rect x="300" y="129" width="27" height="9" rx="4.5"/>
      <rect x="336" y="129" width="72" height="9" rx="4.5"/>
      <rect x="104" y="145" width="50" height="4" rx="2"/>
      <rect x="104" y="155" width="50" height="4" rx="2"/>
      <rect x="104" y="165" width="50" height="4" rx="2"/>
      <rect x="772" y="158" width="104" height="9" rx="4.5"/>
      <rect x="772" y="174" width="72" height="9" rx="4.5"/>
      <rect x="772" y="191" width="29" height="9" rx="4.5"/>
      <rect x="811" y="191" width="70" height="9" rx="4.5"/>
      <rect x="1000" y="217" width="44" height="4" rx="2"/>
      <rect x="1000" y="227" width="44" height="4" rx="2"/>
      <rect x="1000" y="237" width="44" height="4" rx="2"/>
    </g>
  </svg>

  <div class="topics">
    <span class="topics__mark" aria-hidden="true">”</span>
    <ul class="topics__list">
      <li>Büchern</li>
      <li>Film</li>
      <li>Kino</li>
      <li>Altertum</li>
    </ul>
  </div>

  <div class="brand">
    <span class="brand__dot" aria-hidden="true"></span>
    <span class="brand__name">Sinnesfaden</span>
  </div>
</div>
</body>
</html>
```